Webbanner-Design für Beteiligungsunternehmen
Zielgruppe
Ich habe ein kleines Familieninternes Beteiligungsunternehmen welches an verschiedenen Firmen beteiligt ist.
Aufgabenstellung
Ich brauche ein Profilbanner für Facebook und Twitter welches zum einen meine Hauptmarke 'Mertlow Holding' und meine Unternehmen an denen ich beteiligt bin (Geldwacht/Kaldoran Real Estate/ TK Holding/Brivalo) zeigt.

```html
<!DOCTYPE html>
<html lang="de">
<head>
<meta charset="utf-8">
<title>Mertlow Holding – Profilbanner</title>
<link rel="stylesheet" href="https://fonts.googleapis.com/css2?family=Orbitron:wght@500;700&display=swap">
<style>
  :root {
    --brand-brown: #6b2914;
    --band-grey: #818181;
    --paper: #ffffff;
    --on-band: #ffffff;
    --shadow: rgba(0, 0, 0, 0.45);
  }
  * { box-sizing: border-box; margin: 0; padding: 0; }
  html, body {
    width: 1200px;
    height: 845px;
    overflow: hidden;
    background: var(--paper);
  }
  .canvas {
    position: relative;
    width: 1200px;
    height: 845px;
  }
  .banner {
    position: absolute;
    background: var(--paper);
    box-shadow: 0 0 12px var(--shadow);
  }
  .banner--facebook {
    left: 319px; top: 79px; width: 558px; height: 212px;
    --mark-size: 60px;
    --mark-top: 31px;
    --title-size: 32px;
    --title-top: 104px;
    --partner-size: 9px;
    --band-height: 53px;
  }
  .banner--twitter {
    left: 88px; top: 422px; width: 1020px; height: 340px;
    --mark-size: 110px;
    --mark-top: 33px;
    --title-size: 60px;
    --title-top: 166px;
    --partner-size: 17px;
    --band-height: 99px;
  }
  .brand__mark {
    position: absolute;
    left: 50%;
    top: var(--mark-top);
    width: var(--mark-size);
    height: var(--mark-size);
    transform: translateX(-50%);
    background: var(--brand-brown);
  }
  .brand__name {
    position: absolute;
    left: 50%;
    top: var(--title-top);
    transform: translateX(-50%);
    font-family: "Orbitron", sans-serif;
    font-weight: 700;
    font-size: var(--title-size);
    line-height: 1;
    letter-spacing: 0;
    text-transform: uppercase;
    color: var(--brand-brown);
    white-space: nowrap;
  }
  .partners {
    position: absolute;
    left: 0; right: 0; bottom: 0;
    height: var(--band-height);
    background: var(--band-grey);
    display: grid;
    grid-template-columns: repeat(4, 1fr);
    align-items: center;
    padding: 0 3%;
  }
  .partner {
    justify-self: center;
    font-family: "Orbitron", sans-serif;
    font-weight: 500;
    font-size: var(--partner-size);
    letter-spacing: 0.05em;
    text-transform: uppercase;
    color: var(--on-band);
    white-space: nowrap;
    text-align: center;
  }
</style>
</head>
<body>
<main class="canvas">
  <section class="banner banner--facebook" aria-label="Facebook-Profilbanner">
    <div class="brand__mark" role="img" aria-label="Platz für die Bildmarke von Mertlow Holding"></div>
    <h1 class="brand__name">Mertlow Holding</h1>
    <div class="partners">
      <span class="partner">Geldwacht</span>
      <span class="partner">Kaldoran Real Estate</span>
      <span class="partner">Brivalo</span>
      <span class="partner">TK Holding</span>
    </div>
  </section>

  <section class="banner banner--twitter" aria-label="Twitter-Profilbanner">
    <div class="brand__mark" role="img" aria-label="Platz für die Bildmarke von Mertlow Holding"></div>
    <h2 class="brand__name">Mertlow Holding</h2>
    <div class="partners">
      <span class="partner">Geldwacht</span>
      <span class="partner">Kaldoran Real Estate</span>
      <span class="partner">Brivalo</span>
      <span class="partner">TK Holding</span>
    </div>
  </section>
</main>
</body>
</html>
```